Food Safety 1-California workers only

3.25" by 4.5" Black and White Magazine Ad
This ad is to train California workers only.
Workers will be trained on: Food Safety, FSMA (Food Safety Modernization Act), using equipment safety, food processing production skills, worker safety, supervisory skills, communication skills.
"FREE TRAINING", The company does the training or Keystone Learning will provide the training.
Training grants range from $100,000 to $400,000.
Companies must be in business for profit.
Companies must train 200 employees or more.
This program is for California workers only.
Incumbent or new-hires are eligible.

Target Market(s)

California food processors, farms, food packaging, food processors, companies under FSMA, food safety, food production who need to train employees.

Industry/Entity Type

Food Production

Font styles to use
Serif
Sans Serif

Colors

Designer to choose colors to be used in the design.

Requirements
Must have
• This is a 3.25 inch by 4.5 inch magazine ad. It must be black and white. No color.
• The deliverable must be in basic PhotoShop. The ad does not need to include any graphics and be text only if needed. If you have a black and white graphic that will show well.
• Look at www.KLGFoodSafety..com
• Use the text from "MEALBOX-Photoshop-052018" file as your starting point.
Nice to have
• A black and white graphic about food. See www.KLGFoodSafety.com
Should not have
• No color.

```html
<!DOCTYPE html>
<html lang="en">
<head>
<meta charset="utf-8">
<title>Free Training – Keystone Learning</title>
<link href="https://fonts.googleapis.com/css2?family=Playfair+Display:wght@400;700;900&family=Open+Sans:wght@400;600;700&display=swap" rel="stylesheet">
<style>
  :root {
    --ink: #111111;
    --dark: #2a2a2a;
    --mid: #6e6e6e;
    --light: #bdbdbd;
    --paper: #ffffff;
  }
  * { box-sizing: border-box; margin: 0; padding: 0; }
  html, body { width: 867px; height: 1200px; overflow: hidden; background: var(--paper); }
  .ad {
    position: relative; width: 867px; height: 1200px; overflow: hidden;
    background: var(--paper); color: var(--ink);
    font-family: "Open Sans", Arial, sans-serif;
  }
  .headline-band {
    position: absolute; top: 0; left: 0; width: 100%; height: 98px;
    background: var(--ink); color: var(--paper);
    display: flex; align-items: center; justify-content: center;
  }
  .headline {
    font-family: "Playfair Display", Georgia, serif; font-weight: 900;
    font-size: 80px; letter-spacing: 2px; line-height: 1;
  }
  .produce-photo {
    position: absolute; top: 98px; right: 0; width: 470px; height: 360px;
    background: linear-gradient(90deg, var(--paper) 0%, #d9d9d9 22%, #8a8a8a 55%, #4a4a4a 100%);
  }
  .topics {
    position: absolute; top: 134px; left: 36px; list-style: none;
  }
  .topics li {
    display: flex; align-items: center; gap: 18px; height: 62px;
    font-family: "Playfair Display", Georgia, serif; font-weight: 700; font-size: 40px;
  }
  .tick { width: 40px; height: 40px; flex: none; }
  .swoosh { position: absolute; top: 360px; left: 0; width: 867px; height: 170px; }
  .pitch {
    position: absolute; top: 522px; left: 0; width: 100%; text-align: center;
    font-family: "Playfair Display", Georgia, serif;
  }
  .pitch-line1 { font-size: 40px; font-weight: 400; line-height: 1.15; }
  .pitch-line2 { font-size: 40px; font-weight: 900; line-height: 1.15; }
  .quote-mark {
    position: absolute; font-family: "Playfair Display", Georgia, serif;
    font-weight: 900; font-size: 66px; color: var(--mid); line-height: 1;
  }
  .quote-open { left: 44px; top: -8px; }
  .quote-close { right: 26px; top: 44px; }
  .qualify-title {
    position: absolute; top: 660px; left: 60px; right: 60px;
    display: flex; align-items: center; gap: 20px;
    font-family: "Playfair Display", Georgia, serif; font-weight: 700;
    font-size: 28px; letter-spacing: 3px; white-space: nowrap; line-height: 1.2;
  }
  .qualify-title::before, .qualify-title::after {
    content: ""; flex: 1; height: 3px; background: var(--ink);
  }
  .criteria {
    position: absolute; top: 712px; list-style: none; font-size: 20px; line-height: 1.3;
  }
  .criteria-left { left: 48px; width: 400px; }
  .criteria-right { left: 470px; width: 370px; }
  .criteria li { display: flex; gap: 12px; margin-bottom: 10px; }
  .criteria .tick { width: 22px; height: 22px; margin-top: 3px; }
  .contact-card {
    position: absolute; top: 922px; left: 44px; width: 779px; height: 266px;
    border: 3px dashed var(--light); border-radius: 26px;
    padding-top: 26px; text-align: center;
  }
  .contact-tab {
    position: absolute; top: -30px; left: 50%; transform: translateX(-50%);
    background: var(--ink); color: var(--paper); border-radius: 10px;
    padding: 4px 40px; font-family: "Playfair Display", Georgia, serif;
    font-weight: 700; font-size: 30px; white-space: nowrap; line-height: 1.3;
  }
  .contact-name { font-weight: 700; font-size: 34px; letter-spacing: 1px; line-height: 1.3; }
  .contact-company { font-weight: 600; font-size: 24px; color: var(--mid); margin-bottom: 6px; line-height: 1.35; }
  .contact-line {
    display: flex; align-items: center; justify-content: center; gap: 10px;
    font-size: 20px; line-height: 1.4;
  }
  .contact-line svg { width: 19px; height: 19px; flex: none; }
</style>
</head>
<body>
<div class="ad">
  <header class="headline-band"><h1 class="headline">FREE TRAINING</h1></header>

  <div class="produce-photo" role="img" aria-label="Black and white photo of fresh vegetables in a wooden crate"></div>

  <ul class="topics">
    <li><svg class="tick" viewBox="0 0 40 40"><circle cx="20" cy="20" r="17" fill="none" stroke="#111" stroke-width="2.5"/><path d="M12 20l6 6 11-13" fill="none" stroke="#111" stroke-width="3"/></svg>Food Safety</li>
    <li><svg class="tick" viewBox="0 0 40 40"><circle cx="20" cy="20" r="17" fill="none" stroke="#111" stroke-width="2.5"/><path d="M12 20l6 6 11-13" fill="none" stroke="#111" stroke-width="3"/></svg>FSMA</li>
    <li><svg class="tick" viewBox="0 0 40 40"><circle cx="20" cy="20" r="17" fill="none" stroke="#111" stroke-width="2.5"/><path d="M12 20l6 6 11-13" fill="none" stroke="#111" stroke-width="3"/></svg>Production Skills</li>
    <li><svg class="tick" viewBox="0 0 40 40"><circle cx="20" cy="20" r="17" fill="none" stroke="#111" stroke-width="2.5"/><path d="M12 20l6 6 11-13" fill="none" stroke="#111" stroke-width="3"/></svg>Worker Safety</li>
  </ul>

  <svg class="swoosh" viewBox="0 0 867 190" preserveAspectRatio="none" aria-hidden="true">
    <path d="M0 40 C220 120 520 110 867 40 L867 98 C560 170 250 170 0 120 Z" fill="#111"/>
    <path d="M0 70 C240 140 540 130 867 70 L867 86 C540 150 240 158 0 92 Z" fill="#fff"/>
    <path d="M0 150 C260 190 560 180 867 120" fill="none" stroke="#bdbdbd" stroke-width="3"/>
  </svg>

  <section class="pitch">
    <span class="quote-mark quote-open">&ldquo;</span>
    <p class="pitch-line1">You Do The Training And</p>
    <p class="pitch-line2">The State Of &nbsp;California Pays For It!</p>
    <span class="quote-mark quote-close">&rdquo;</span>
  </section>

  <h2 class="qualify-title">HOW TO QUALIFY</h2>

  <ul class="criteria criteria-left">
    <li><svg class="tick" viewBox="0 0 40 40"><circle cx="20" cy="20" r="17" fill="none" stroke="#111" stroke-width="3"/><path d="M12 20l6 6 11-13" fill="none" stroke="#111" stroke-width="4"/></svg>Train California Workers Only</li>
    <li><svg class="tick" viewBox="0 0 40 40"><circle cx="20" cy="20" r="17" fill="none" stroke="#111" stroke-width="3"/><path d="M12 20l6 6 11-13" fill="none" stroke="#111" stroke-width="4"/></svg>Trainees must earn $11/hour</li>
    <li><svg class="tick" viewBox="0 0 40 40"><circle cx="20" cy="20" r="17" fill="none" stroke="#111" stroke-width="3"/><path d="M12 20l6 6 11-13" fill="none" stroke="#111" stroke-width="4"/></svg>Full-time workers only</li>
    <li><svg class="tick" viewBox="0 0 40 40"><circle cx="20" cy="20" r="17" fill="none" stroke="#111" stroke-width="3"/><path d="M12 20l6 6 11-13" fill="none" stroke="#111" stroke-width="4"/></svg>Employees must attend at least 8 Hours of training</li>
  </ul>
  <ul class="criteria criteria-right">
    <li><svg class="tick" viewBox="0 0 40 40"><circle cx="20" cy="20" r="17" fill="none" stroke="#111" stroke-width="3"/><path d="M12 20l6 6 11-13" fill="none" stroke="#111" stroke-width="4"/></svg>You must train 200 or more employees</li>
    <li><svg class="tick" viewBox="0 0 40 40"><circle cx="20" cy="20" r="17" fill="none" stroke="#111" stroke-width="3"/><path d="M12 20l6 6 11-13" fill="none" stroke="#111" stroke-width="4"/></svg>Incumbent or New-Hire workers are eligible</li>
    <li><svg class="tick" viewBox="0 0 40 40"><circle cx="20" cy="20" r="17" fill="none" stroke="#111" stroke-width="3"/><path d="M12 20l6 6 11-13" fill="none" stroke="#111" stroke-width="4"/></svg>Seasonal workers are eligible</li>
  </ul>

  <section class="contact-card">
    <div class="contact-tab">Contact Us</div>
    <p class="contact-name">DANIEL MARSH</p>
    <p class="contact-company">KEYSTONE LEARNING COMPANY, INC.</p>
    <p class="contact-line"><svg viewBox="0 0 20 20"><path d="M10 1a6 6 0 0 0-6 6c0 5 6 12 6 12s6-7 6-12a6 6 0 0 0-6-6z" fill="#6e6e6e"/><circle cx="10" cy="7" r="2.2" fill="#fff"/></svg>1250 Harbor Crest Drive, Suite 310, Irvine, CA 92618</p>
    <p class="contact-line"><svg viewBox="0 0 20 20"><circle cx="10" cy="10" r="8" fill="none" stroke="#6e6e6e" stroke-width="1.8"/><path d="M2 10h16M10 2c-4 5-4 11 0 16M10 2c4 5 4 11 0 16" fill="none" stroke="#6e6e6e" stroke-width="1.4"/></svg>www.KLGCAL.com, www.KLGFoodSafety.com</p>
    <p class="contact-line"><svg viewBox="0 0 20 20"><rect x="2" y="4" width="16" height="12" rx="1.5" fill="none" stroke="#6e6e6e" stroke-width="1.8"/><path d="M2 5l8 6 8-6" fill="none" stroke="#6e6e6e" stroke-width="1.6"/></svg>Dan.Marsh@KLGCAL.com</p>
    <p class="contact-line"><svg viewBox="0 0 20 20"><path d="M5 2l3 4-2 2c1 2.5 3.5 5 6 6l2-2 4 3-2 3C9 18 2 11 2 4z" fill="#6e6e6e"/></svg>(949) 555-0147</p>
  </section>
</div>
</body>
</html>
```